Corvellan Solutions needs an IT Managed Services Website and the logo needs to be updated

We need a new website for our 25 year old IT Managed Services Company. Our company specializes in listening to and understanding our customer needs and goals. Our customers include SME's and Corporates in industries ranging from Medical, Legal, Industrial & Manufacturing and Financial. The services that we offer include: Managed IT Services, Remote Monitoring and Management and Virtualisation. Corvellan Solutions takes technology and makes the lives of our customers easier by applying it appropriately. In the same way, we want a website that is as pleasing to the eye, as it is simple to find information and call to action. The website should say as much in design as it does in content and it should be saying that Corvellan Solutions is your technology partner that listens to you, understands you, delivers solutions and is loyal in our relationship with you. Aesthetically, we want to go for something a little warmer than blue and white, but want to err on the side of professional.
The Logo: We need the "computer" and "ltd" to be removed from the logo. We want to keep the @ on the "u". We would like to freshen up the logo inline with the website design in terms of look and feel and colour.

Target Market(s)

Businesses that require IT Managed Services

Logo Text

Corvellan Solutions

Coding

Coded - Design and coding required

Number of Pages Required

5+ page

Font styles to use
Sans Serif

Colors

Designer to choose colors to be used in the design.

Requirements
Must have
• Each page must have a call to action.

```html
<!DOCTYPE html>
<html lang="en">
<head>
<meta charset="utf-8">
<title>Corvellan Solutions – IT Managed Services</title>
<link href="https://fonts.googleapis.com/css2?family=Montserrat:wght@400;500;600;700&family=Open+Sans:ital,wght@0,400;0,600;1,400&display=swap" rel="stylesheet">
<style>
:root{
  --navy:#12275c;
  --navy-deep:#0a1838;
  --navy-mid:#1a3a80;
  --gold:#f0b31a;
  --gold-dark:#e0a000;
  --ink:#333a44;
  --muted:#555c66;
  --white:#ffffff;
  --line:#d9dde3;
}
*{box-sizing:border-box;margin:0;padding:0}
html,body{width:1200px;height:3141px;overflow:hidden}
body{font-family:"Open Sans",Arial,sans-serif;color:var(--ink);background:var(--white);position:relative}
.section{position:absolute;left:0;width:1200px}
.gold-rule{display:block;width:84px;height:3px;background:var(--gold)}
.btn{display:inline-flex;align-items:center;justify-content:center;background:var(--gold);color:var(--white);font-family:"Montserrat",Arial,sans-serif;font-weight:700;text-transform:uppercase;text-decoration:none}

/* header + hero */
.hero{top:0;height:572px;background:linear-gradient(160deg,#1d3f8f 0%,#16337a 45%,#0e2459 100%)}
.hero-photo{position:absolute;inset:0;background:radial-gradient(ellipse at 78% 55%,rgba(120,150,220,.35),transparent 55%),radial-gradient(ellipse at 20% 30%,rgba(80,110,190,.25),transparent 50%)}
.topbar{position:absolute;top:0;left:0;right:0;height:63px;color:var(--white);font-size:16px}
.topbar .email{position:absolute;left:86px;top:22px;display:flex;align-items:center;gap:12px}
.topbar .address{position:absolute;left:833px;top:10px;display:flex;gap:12px;line-height:24px}
.navbar{position:absolute;top:63px;left:0;right:0;height:56px;background:rgba(8,20,52,.55)}
.brand{position:absolute;left:86px;top:8px;font-family:"Montserrat",Arial,sans-serif;font-size:31px;font-weight:400;color:var(--white);line-height:40px}
.nav{position:absolute;right:86px;top:0;display:flex;list-style:none;height:56px}
.nav li{font-family:"Montserrat",Arial,sans-serif;font-size:13px;font-weight:500;color:var(--white);padding:0 22px;line-height:56px}
.nav li.active{background:var(--gold)}
.hero-title{position:absolute;top:228px;left:0;width:1200px;text-align:center;font-family:"Montserrat",Arial,sans-serif;font-weight:700;font-size:44px;line-height:54px;color:var(--gold);text-transform:uppercase}
.hero-phone{position:absolute;top:355px;left:0;width:1200px;display:flex;justify-content:center;align-items:center;gap:14px;font-family:"Montserrat",Arial,sans-serif;font-size:32px;color:var(--white)}
.hero-cta{position:absolute;top:417px;left:500px;width:199px;height:36px;font-size:15px}

/* about */
.about{top:572px;height:485px}
.about-heading{position:absolute;left:86px;top:50px;font-family:"Montserrat",Arial,sans-serif;color:var(--ink);font-size:33px;line-height:42px;text-transform:uppercase;font-weight:400}
.about-heading .num{color:var(--gold);font-weight:700;font-size:60px;vertical-align:-4px}
.about .gold-rule{position:absolute;left:86px;top:165px}
.body-text{font-size:13.5px;line-height:21px;color:var(--muted)}
.about-text{position:absolute;left:86px;top:208px;width:600px}
.about-btn{position:absolute;left:86px;top:370px;width:142px;height:36px;font-size:12px}
.about-frame{position:absolute;left:806px;top:64px;width:308px;height:360px;border:1px solid var(--line);background:var(--white)}
.about-photo{position:absolute;left:836px;top:86px;width:278px;height:337px;background:linear-gradient(135deg,#b6733f 0%,#7c4a2c 40%,#2a3e5a 100%)}
.about-inset{position:absolute;left:773px;top:233px;width:140px;height:158px;border:4px solid var(--white);background:linear-gradient(140deg,#f0a23a,#d4641c)}

/* services */
.services{top:1057px;height:572px;background:linear-gradient(180deg,#102657,#0c1f4a)}
.services-device{position:absolute;left:147px;top:178px;width:293px;height:356px;border-radius:24px;background:linear-gradient(160deg,#2a3342 0%,#151b24 60%,#c99a7c 100%);opacity:.95}
.services-title{position:absolute;left:632px;top:60px;font-family:"Montserrat",Arial,sans-serif;font-size:31px;color:var(--white);font-weight:500;text-transform:uppercase}
.services .gold-rule{position:absolute;left:632px;top:108px}
.svc{position:absolute;left:632px;width:482px;border:1px solid rgba(255,255,255,.55)}
.svc-head{height:42px;display:flex;align-items:center;padding-left:52px;position:relative;font-family:"Montserrat",Arial,sans-serif;font-size:13px;font-weight:600;color:var(--white);text-transform:uppercase}
.svc-icon{position:absolute;left:0;top:0;width:42px;height:42px;background:var(--white);display:flex;align-items:center;justify-content:center}
.svc.open .svc-icon{background:var(--gold)}
.svc.open .svc-head{color:var(--gold)}
.svc-btn{position:absolute;right:6px;top:6px;width:136px;height:30px;font-size:10px}
.svc-body{border-top:1px solid rgba(255,255,255,.55);padding:14px 26px;color:var(--white);font-size:13.5px;line-height:21px}

/* why */
.why{top:1629px;height:549px}
.why-title{position:absolute;left:86px;top:56px;font-family:"Montserrat",Arial,sans-serif;font-size:31px;font-weight:500;color:var(--ink);text-transform:uppercase}
.why .gold-rule{position:absolute;left:86px;top:101px}
.why-text{position:absolute;left:86px;top:137px;width:540px}
.why-text p{margin-bottom:21px}
.why-btn{position:absolute;left:86px;top:437px;width:134px;height:33px;font-size:12px}
.why-img-back{position:absolute;left:746px;top:82px;width:368px;height:390px;background:linear-gradient(150deg,#cfd9e4 0%,#5a8ca8 40%,#1f5a6e 100%)}
.why-img-front{position:absolute;left:680px;top:176px;width:298px;height:300px;border:4px solid var(--white);background:linear-gradient(160deg,#7fd1dd,#2b8fa3 60%,#14596b)}

/* testimonial */
.testimonial{top:2178px;height:419px;background:linear-gradient(180deg,#0f2a66,#0a1d48);text-align:center;color:var(--white)}
.t-title{position:absolute;top:52px;left:0;width:1200px;font-family:"Montserrat",Arial,sans-serif;font-size:31px;font-weight:500;text-transform:uppercase}
.testimonial .gold-rule{position:absolute;left:558px;top:96px}
.t-quote{position:absolute;top:134px;left:583px}
.t-text{position:absolute;top:200px;left:200px;width:800px;font-style:italic;font-size:13.5px;line-height:22px}
.t-author{position:absolute;top:314px;left:0;width:1200px;font-size:13px}
.t-author b{font-family:"Montserrat",Arial,sans-serif;font-weight:700;letter-spacing:.5px}
.t-dots{position:absolute;top:351px;left:580px;display:flex;gap:8px}
.t-dots span{width:9px;height:9px;border:1px solid var(--white)}
.t-dots span.on{background:var(--gold);border-color:var(--gold)}

/* partners */
.partners{top:2597px;height:278px;text-align:center}
.p-title{position:absolute;top:52px;left:0;width:1200px;font-family:"Montserrat",Arial,sans-serif;font-size:31px;font-weight:500;color:var(--ink);text-transform:uppercase}
.partners .gold-rule{position:absolute;left:558px;top:98px}
.p-row{position:absolute;top:146px;left:246px;display:flex;gap:10px;align-items:center}
.p-arrow{width:22px;height:22px;background:#cfd2d6;display:flex;align-items:center;justify-content:center;margin:0 32px}
.p-badge{width:149px;height:74px;background:var(--white);box-shadow:0 2px 6px rgba(0,0,0,.25);display:flex;align-items:center;justify-content:center}
.p-badge span{display:block;width:92px;height:26px;border-radius:4px;background:#c7ccd3}

/* footer */
.footer{top:2875px;height:266px;background:linear-gradient(180deg,#0f2352,#0a1a3e);color:var(--white)}
.f-brand{position:absolute;left:86px;top:102px;font-family:"Montserrat",Arial,sans-serif;font-size:31px;line-height:40px}
.f-copy{position:absolute;left:86px;top:157px;font-size:14px}
.f-head{position:absolute;font-family:"Montserrat",Arial,sans-serif;font-size:15px;font-weight:700;text-transform:uppercase}
.f-contact{position:absolute;left:574px;top:88px;list-style:none;font-size:15px}
.f-contact li{display:flex;gap:12px;align-items:flex-start;line-height:23px;margin-bottom:7px}
.f-contact svg{flex:none;margin-top:4px}
.f-links{position:absolute;left:1002px;top:78px;list-style:none;font-size:15px}
.f-links li{line-height:31px}
</style>
</head>
<body>

<header class="section hero">
  <div class="hero-photo" role="img" aria-label="Close-up of hands typing on a laptop keyboard with faint gear shapes, tinted blue"></div>
  <div class="topbar">
    <div class="email">
      <svg width="26" height="18" viewBox="0 0 26 18"><rect x="1" y="1" width="24" height="16" fill="none" stroke="#fff" stroke-width="2"/><path d="M1 1l12 9 12-9" fill="none" stroke="#fff" stroke-width="2"/></svg>
      info@corvellansolutions.com
    </div>
    <div class="address">
      <svg width="14" height="20" viewBox="0 0 14 20" style="margin-top:2px"><path d="M7 0a7 7 0 0 1 7 7c0 5-7 13-7 13S0 12 0 7a7 7 0 0 1 7-7z" fill="#fff"/><circle cx="7" cy="7" r="2.6" fill="#16337a"/></svg>
      <span>42 Harrow Ave., Suite 310 Ridgefield,<br>Ontario, L9Z 2K7</span>
    </div>
  </div>
  <nav class="navbar">
    <div class="brand">Corvellan Solutions</div>
    <ul class="nav">
      <li class="active">HOME</li>
      <li>ABOUT US</li>
      <li>SERVICES</li>
      <li>WHY CHOOSE US</li>
      <li>CONTACT US</li>
    </ul>
  </nav>
  <h1 class="hero-title">Remote Monitoring &amp; Management &amp;<br>Virtualisation</h1>
  <div class="hero-phone">
    <svg width="24" height="24" viewBox="0 0 24 24"><path d="M6 2l4 5-2 3c1.5 3 3.5 5 6 6l3-2 5 4-3 4C10 22 2 14 2 5z" fill="#f0b31a"/></svg>
    555.214.0190
  </div>
  <a class="btn hero-cta">Contact us now</a>
</header>

<section class="section about">
  <h2 class="about-heading"><span class="num">25</span> Year old IT managed<br>services company</h2>
  <span class="gold-rule"></span>
  <p class="body-text about-text">Corvellan Solutions is an IT Managed Services Provider (MSP) that has more than 25 years experience growing and collaborating in the IT Industry. Our expertise lies in listening to and understanding our more than 1000 customers' needs and delivering the best value for money IT Infrastructure and Technology solutions. We believe in loyal and lasting relationships creating a matrix within which your company can grow and outperform it's own expectations.</p>
  <a class="btn about-btn">Read more</a>
  <div class="about-frame"></div>
  <div class="about-photo" role="img" aria-label="Photo of two colleagues working together at a computer"></div>
  <div class="about-inset" role="img" aria-label="Illustration of a tablet with ideas and charts on an orange background"></div>
</section>

<section class="section services">
  <div class="services-device" role="img" aria-label="Hand holding a smartphone showing the website on its screen"></div>
  <h2 class="services-title">Our services</h2>
  <span class="gold-rule"></span>

  <div class="svc open" style="top:145px">
    <div class="svc-head">
      <span class="svc-icon"><svg width="24" height="20" viewBox="0 0 24 20"><rect x="1" y="1" width="22" height="14" fill="none" stroke="#fff" stroke-width="2"/><path d="M8 19h8M12 15v4" stroke="#fff" stroke-width="2"/></svg></span>
      Remote monitoring
      <a class="btn svc-btn">Contact us now</a>
    </div>
    <div class="svc-body">Corvellan brings you an all-encompassing service that includes managed antivirus, web protection, backup &amp; recovery and email security. You will be able to manage all devices including mobile and you will have active discovery on the network - identifying and managing all new devices that come onto the network</div>
  </div>

  <div class="svc" style="top:379px">
    <div class="svc-head">
      <span class="svc-icon"><svg width="24" height="24" viewBox="0 0 24 24"><circle cx="12" cy="8" r="4" fill="none" stroke="#12275c" stroke-width="2"/><path d="M4 22c1-5 4-7 8-7s7 2 8 7" fill="none" stroke="#12275c" stroke-width="2"/></svg></span>
      IT management
      <a class="btn svc-btn">Contact us now</a>
    </div>
  </div>

  <div class="svc" style="top:465px">
    <div class="svc-head">
      <span class="svc-icon"><svg width="24" height="24" viewBox="0 0 24 24"><circle cx="12" cy="12" r="4" fill="none" stroke="#12275c" stroke-width="2"/><path d="M12 2v4M12 18v4M2 12h4M18 12h4M5 5l3 3M16 16l3 3M5 19l3-3M16 8l3-3" stroke="#12275c" stroke-width="2"/></svg></span>
      Virtualisation
      <a class="btn svc-btn">Contact us now</a>
    </div>
  </div>
</section>

<section class="section why">
  <h2 class="why-title">Why choose us</h2>
  <span class="gold-rule"></span>
  <div class="body-text why-text">
    <p>Corvellan Solutions was founded in 2000 and is in the business of collaborating with partners to bring the best technologies to you.</p>
    <p>We have more than 25 years experience in the IT industry, servicing customers across the GTA and Ontario. Our customers come from different industry sectors including Medical, Financial, Real Estate, Legal and more. We work together with our customers as members of their teams to realize their IT visions and goals.</p>
    <p>We have collaborated with partners across the globe to ensure that we bring the most innovate and functional technology to our customers. We can proudly say that we offer the best Value for Money solutions.</p>
  </div>
  <a class="btn why-btn">Read more</a>
  <div class="why-img-back" role="img" aria-label="Hand touching a network of connected people icons"></div>
  <div class="why-img-front" role="img" aria-label="Tablet with a glowing globe and technology interface graphics"></div>
</section>

<section class="section testimonial">
  <h2 class="t-title">Testimonial</h2>
  <span class="gold-rule"></span>
  <svg class="t-quote" width="34" height="26" viewBox="0 0 34 26"><path d="M2 26V14C2 6 6 1 14 0v5c-4 1-6 4-6 8h6v13zM20 26V14c0-8 4-13 12-14v5c-4 1-6 4-6 8h6v13z" fill="#fff"/></svg>
  <p class="t-text">Lorem Ipsum is simply dummy text of the printing and typesetting industry. Lorem Ipsum has been the industry's standard dummy text ever since the 1500s, when an unknown printer took a galley of type and scrambled it to make a type specimen book. It has survived not only five centuries, but also the leap into electronic typesetting, remaining essentially unchanged. It was popularised in the 1960s with the release of Verilane sheets</p>
  <p class="t-author"><b>DANIEL REYES</b> - CEO, FOUNDER</p>
  <div class="t-dots"><span></span><span class="on"></span><span></span></div>
</section>

<section class="section partners">
  <h2 class="p-title">Our partners</h2>
  <span class="gold-rule"></span>
  <div class="p-row">
    <div class="p-arrow"><svg width="8" height="10" viewBox="0 0 8 10"><path d="M7 0L0 5l7 5z" fill="#555"/></svg></div>
    <div class="p-badge" role="img" aria-label="Partner badge"><span></span></div>
    <div class="p-badge" role="img" aria-label="Partner badge"><span></span></div>
    <div class="p-badge" role="img" aria-label="Partner badge"><span></span></div>
    <div class="p-badge" role="img" aria-label="Partner badge"><span></span></div>
    <div class="p-arrow"><svg width="8" height="10" viewBox="0 0 8 10"><path d="M1 0l7 5-7 5z" fill="#555"/></svg></div>
  </div>
</section>

<footer class="section footer">
  <div class="f-brand">Corvellan Solutions</div>
  <p class="f-copy">Copyright © 2018 &nbsp;|&nbsp; All Rights Reserved.</p>
  <h3 class="f-head" style="left:574px;top:38px">Contact us</h3>
  <ul class="f-contact">
    <li><svg width="13" height="18" viewBox="0 0 14 20"><path d="M7 0a7 7 0 0 1 7 7c0 5-7 13-7 13S0 12 0 7a7 7 0 0 1 7-7z" fill="#fff"/><circle cx="7" cy="7" r="2.6" fill="#0f2352"/></svg><span>42 Harrow Ave., Suite 310 Ridgefield,<br>Ontario, L9Z 2K7</span></li>
    <li><svg width="16" height="16" viewBox="0 0 24 24"><path d="M6 2l4 5-2 3c1.5 3 3.5 5 6 6l3-2 5 4-3 4C10 22 2 14 2 5z" fill="#fff"/></svg>555.214.0190</li>
    <li><svg width="16" height="16" viewBox="0 0 16 16"><rect x="1" y="5" width="14" height="10" fill="#fff"/><rect x="4" y="1" width="8" height="5" fill="none" stroke="#fff" stroke-width="1.5"/></svg>555.214.0191</li>
    <li><svg width="17" height="13" viewBox="0 0 26 18"><rect x="0" y="0" width="26" height="18" fill="#fff"/><path d="M0 0l13 10 13-10" fill="none" stroke="#0f2352" stroke-width="2"/></svg>info@corvellansolutions.com</li>
  </ul>
  <h3 class="f-head" style="left:1002px;top:38px">Quick links</h3>
  <ul class="f-links">
    <li>Home</li>
    <li>About Us</li>
    <li>Services</li>
    <li>Why choose us</li>
    <li>Contact Us</li>
  </ul>
</footer>

</body>
</html>
```